Healthcare technology company needs website design

We need a logo for a new company based in the U.S. We develop software to assist consumers identifying lowest cost healthcare coverage methods, including insurance, discount cards, and cash options. We would like to see designs that use multiple shades of green with the optional addition of other complimentary colors. The final design should communicate a unique blend of saving money while receiving the healthcare you need.
Need the following pages/sections: Homepage, Solutions, About Us, Contact
Competitors: www.velorinhealth.example; www.qdplm.example

Target Market(s)

Businesses

Industry/Entity Type

Healthcare

Coding

Coded - Design and coding required

Number of Pages Required

4 page

Colors
0054AA
0677BA
7BADD7
CADEEF
E8F1F8
00AB8E
00BBA5
67D7C9
C6EFE9
E9F9F6

Requirements
Must have
• Matching color theme with logo
Nice to have
• Animated background

```html
<!DOCTYPE html>
<html lang="en">
<head>
<meta charset="utf-8">
<title>Evergrove Health</title>
<link rel="stylesheet" href="https://fonts.googleapis.com/css2?family=Montserrat:wght@400;500;600;700&display=swap">
<style>
:root{
  --blue-deep:#0054AA;
  --blue:#0677BA;
  --blue-soft:#7BADD7;
  --blue-pale:#CADEEF;
  --blue-mist:#E8F1F8;
  --green-deep:#00AB8E;
  --green:#00BBA5;
  --green-mid:#67D7C9;
  --green-pale:#C6EFE9;
  --green-mist:#E9F9F6;
  --ink:#111;
  --white:#fff;
}
*{margin:0;padding:0;box-sizing:border-box}
html,body{width:1200px;height:3596px;overflow:hidden;background:var(--white)}
body{font-family:'Montserrat',sans-serif;color:var(--ink);position:relative}
.abs{position:absolute}

/* hero */
.hero{left:0;top:0;width:1200px;height:600px;
  background:linear-gradient(120deg,#e9edf3 0%,#eef1f5 35%,#e4cfc4 55%,#e8ecf2 75%,#eef1f6 100%)}
.brand{left:50px;top:48px;display:flex;align-items:center;gap:18px}
.brand-dot{width:70px;height:70px;border-radius:50%;background:var(--green-deep)}
.brand-name{font-size:44px;font-weight:700;color:var(--green-deep);letter-spacing:2px;line-height:1}
.nav{right:66px;top:32px;display:flex;gap:62px;font-size:19px;font-weight:600}
.hero-bar{left:53px;top:408px;width:11px;height:171px;background:var(--green-mid)}
.hero-title{left:100px;top:404px;font-size:50px;font-weight:500;letter-spacing:4px;line-height:58px;color:#1a1a1a}

/* solution */
.video{left:53px;top:660px;width:649px;height:366px;border-radius:34px;
  background:linear-gradient(135deg,#5b8fc6 0%,#8db4dc 45%,#b9d2ea 100%)}
.play{left:330px;top:790px}
.sol-title{left:746px;top:690px;font-size:50px;font-weight:500;letter-spacing:5px}
.sol-text{left:746px;top:806px;width:300px;font-size:25px;line-height:29px;letter-spacing:1.5px;color:var(--blue-soft)}
.rule{left:57px;top:1081px;width:1003px;height:2px;background:var(--blue-pale)}
.rule-tag{left:1060px;top:1058px;display:flex;align-items:center;gap:8px;font-size:18px;font-weight:700;color:var(--green-deep)}
.rule-tag span{width:40px;height:40px;border-radius:50%;background:var(--green-deep)}

/* benefits */
.ben-title{left:0;top:1205px;width:1200px;text-align:center;font-size:50px;font-weight:500;letter-spacing:5px}
.ben-list{left:103px;top:1377px;width:760px}
.ben-item{height:217px;display:flex;align-items:center;font-size:42px;font-weight:500;position:relative}
.ben-item::before,.ben-item:last-child::after{content:"";position:absolute;left:0;width:497px;height:2px;background:var(--blue-soft)}
.ben-item::before{top:-1px}
.ben-item:last-child::after{bottom:-1px}
.swatches{left:946px;top:1378px;width:216px}
.swatches div{height:217px}

/* call to action */
.cta-photo{left:0;top:2662px;width:760px;height:598px;
  background:linear-gradient(100deg,#2c3b4a 0%,#3e4e5e 40%,#5a6d80 60%,#9bb1cc 80%,rgba(255,255,255,0) 100%)}
.cta-text{right:56px;top:2712px;text-align:right;font-size:31px;line-height:36px;letter-spacing:3px;color:var(--green-mid)}
.join{left:951px;top:3055px;width:196px;height:59px;border-radius:30px;
  background:linear-gradient(90deg,var(--green-deep),var(--green-mid));
  box-shadow:0 3px 8px rgba(0,0,0,.25);color:var(--white);font-size:33px;letter-spacing:4px;
  display:flex;align-items:center;justify-content:center}
.start{right:56px;top:3147px;display:flex;align-items:center;gap:12px;font-size:25px;letter-spacing:1.5px;color:var(--blue-soft)}

/* footer */
.foot-brand{left:60px;top:3378px;font-size:24px;font-weight:700;color:var(--green-deep);width:170px;line-height:28px}
.foot-div{left:251px;top:3292px;width:3px;height:210px;background:var(--blue-pale)}
.foot-col{display:flex;flex-direction:column;gap:40px;font-size:19px;letter-spacing:1px;color:var(--blue)}
.foot-col li{list-style:none;display:flex;align-items:center;gap:24px;height:24px}
.contact{left:290px;top:3295px}
.contact li{gap:36px}
.links1{left:666px;top:3295px}
.links2{left:924px;top:3295px}
.links2{gap:38px}
.bottom{left:0;top:3525px;width:1200px;height:71px;background:var(--blue);color:var(--white);
  font-size:19px;display:flex;align-items:center;justify-content:center;letter-spacing:.5px}
</style>
</head>
<body>

<header class="abs hero" role="img" aria-label="Photo of two hands clasped together on a soft light background"></header>
<div class="abs brand"><span class="brand-dot"></span><span class="brand-name">EVERGROVE HEALTH</span></div>
<nav class="abs nav"><span>SOLUTION</span><span>ABOUT US</span><span>CONTACT</span></nav>
<div class="abs hero-bar"></div>
<h1 class="abs hero-title">Guide You to<br>True Future<br>Healtcare</h1>

<section>
  <div class="abs video" role="img" aria-label="Video still of hands stacking coins on a desk"></div>
  <svg class="abs play" width="96" height="104" viewBox="0 0 96 104"><path d="M10 6 Q0 0 0 14 V90 Q0 104 12 97 L88 58 Q96 52 88 46 Z" fill="#fff"/></svg>
  <h2 class="abs sol-title">SOLUTION</h2>
  <p class="abs sol-text">This is how our technology feature will guide you new experience of true healtcare</p>
  <div class="abs rule"></div>
  <div class="abs rule-tag"><span></span>EG</div>
</section>

<section>
  <h2 class="abs ben-title">BENEFITS</h2>
  <ul class="abs ben-list">
    <li class="ben-item">Real-time Data</li>
    <li class="ben-item">Simplifying Complex Information</li>
    <li class="ben-item">Best Performance</li>
    <li class="ben-item">Transparency Of Cost</li>
    <li class="ben-item">Identifying Trends</li>
  </ul>
  <div class="abs swatches">
    <div style="background:var(--green-mist)"></div>
    <div style="background:var(--green-pale)"></div>
    <div style="background:var(--green-mid)"></div>
    <div style="background:var(--green)"></div>
    <div style="background:var(--green-deep)"></div>
  </div>
</section>

<section>
  <div class="abs cta-photo" role="img" aria-label="Photo of an analytics dashboard screen showing metrics and line charts"></div>
  <p class="abs cta-text">Try our feature<br>And get nwe<br>Experience of<br>True healtcare<br>NOW !</p>
  <div class="abs join">JOIN</div>
  <div class="abs start">
    <svg width="22" height="22" viewBox="0 0 22 22" fill="none" stroke="#7BADD7" stroke-width="2"><path d="M3 3l8 8-8 8M11 3l8 8-8 8"/></svg>
    start services
  </div>
</section>

<footer>
  <div class="abs foot-brand">Evergrove Health</div>
  <div class="abs foot-div"></div>
  <ul class="abs foot-col contact">
    <li><svg width="24" height="24" viewBox="0 0 24 24" fill="none" stroke="#67D7C9" stroke-width="1.6"><path d="M5 3l4 1 1 5-2 2a12 12 0 005 5l2-2 5 1 1 4c0 1-1 2-2 2A18 18 0 013 5c0-1 1-2 2-2z"/></svg>Phone Number</li>
    <li><svg width="24" height="24" viewBox="0 0 24 24" fill="none" stroke="#67D7C9" stroke-width="1.6"><rect x="2" y="5" width="20" height="14" rx="1"/><path d="M2 6l10 7 10-7"/></svg>Email Address</li>
    <li><svg width="24" height="24" viewBox="0 0 24 24" fill="none" stroke="#67D7C9" stroke-width="1.6"><rect x="6" y="2" width="12" height="6"/><rect x="2" y="8" width="20" height="9" rx="1"/><rect x="6" y="14" width="12" height="8"/></svg>Fax</li>
  </ul>
  <ul class="abs foot-col links1">
    <li><svg width="24" height="16" viewBox="0 0 24 16"><path d="M0 8L8 0H24V16H8Z" fill="#67D7C9"/></svg>Solutions</li>
    <li><svg width="24" height="16" viewBox="0 0 24 16"><path d="M0 8L8 0H24V16H8Z" fill="#67D7C9"/></svg>About Us</li>
    <li><svg width="24" height="16" viewBox="0 0 24 16"><path d="M0 8L8 0H24V16H8Z" fill="#67D7C9"/></svg>Contact</li>
  </ul>
  <ul class="abs foot-col links2">
    <li><svg width="24" height="16" viewBox="0 0 24 16"><path d="M0 8L8 0H24V16H8Z" fill="#67D7C9"/></svg>Privacy Policy</li>
    <li><svg width="24" height="16" viewBox="0 0 24 16"><path d="M0 8L8 0H24V16H8Z" fill="#67D7C9"/></svg>Terms and Use</li>
  </ul>
  <div class="abs bottom">2022 Evergrove Health. All rights reserved.</div>
</footer>

</body>
</html>
```